Varemo Group Business Card Design

The CEO is looking for a new trendy look for his business card.
You can stay with current branding or come up with something new/creative. It can be 3D, including Medical Office buildings. You can use our logo in a variety of colors. Please include name, title, company name, company website, email address, cell number

Target Market(s)

Real Estate Development and Construction

Industry/Entity Type

Health care real estate

Contact Information for Business Card

Rohesh Kumbar, CEO M-727.418.9062 E-roheshkumbar@varemo.com Address:4100 Lindell Ave, Tampa, FL 33611 www.varemo.com

Font styles to use
Other font styles liked:
• Be creative

Requirements
Must have
• Creative, trendy look
Nice to have
• Please go to our website to get a feel- www. varemo.com
Should not have
• small fonts

```html
<!DOCTYPE html>
<html lang="en">
<head>
<meta charset="utf-8">
<title>Varemo Group Business Card</title>
<link href="https://fonts.googleapis.com/css2?family=Montserrat:wght@700;800&family=Roboto+Slab:wght@400&display=swap" rel="stylesheet">
<style>
  :root {
    --stage: #262626;
    --card: #151515;
    --red: #b01c24;
    --white: #ffffff;
    --silver: #a3a3a3;
    --ink-soft: #e8e8e8;
  }
  * { margin: 0; padding: 0; box-sizing: border-box; }
  html, body {
    width: 1200px;
    height: 800px;
    overflow: hidden;
    background: var(--stage);
  }
  .stage {
    position: relative;
    width: 1200px;
    height: 800px;
    display: flex;
    align-items: center;
    justify-content: center;
    gap: 40px;
  }
  .card {
    position: relative;
    width: 540px;
    height: 300px;
    border-radius: 18px;
    background: var(--card);
    overflow: hidden;
    box-shadow: 0 18px 40px rgba(0,0,0,0.45);
  }
  .card__accent {
    position: absolute;
    inset: 0;
    width: 100%;
    height: 100%;
  }
  .front__brand {
    position: absolute;
    right: 120px;
    top: 40px;
    font-family: "Montserrat", sans-serif;
    font-weight: 800;
    font-size: 38px;
    letter-spacing: -1px;
    color: var(--red);
    line-height: 1;
  }
  .front__identity {
    position: absolute;
    right: 110px;
    top: 104px;
    text-align: right;
  }
  .front__name {
    font-family: "Montserrat", sans-serif;
    font-weight: 700;
    font-size: 30px;
    color: var(--red);
    line-height: 1.1;
  }
  .front__title {
    margin-top: 6px;
    font-family: "Roboto Slab", serif;
    font-size: 15px;
    color: var(--white);
  }
  .contact {
    position: absolute;
    left: 78px;
    bottom: 26px;
    list-style: none;
    font-family: "Roboto Slab", serif;
    font-size: 13.5px;
    color: var(--ink-soft);
    line-height: 1.45;
  }
  .contact__row {
    display: flex;
    align-items: flex-start;
    gap: 10px;
  }
  .contact__icon {
    width: 12px;
    height: 12px;
    margin-top: 4px;
    flex: none;
    fill: var(--red);
  }
  .contact__icon--empty { visibility: hidden; }
  .back__brand {
    position: absolute;
    inset: 0;
    display: flex;
    align-items: center;
    justify-content: center;
    font-family: "Montserrat", sans-serif;
    font-weight: 800;
    font-size: 54px;
    letter-spacing: -1.5px;
    color: var(--silver);
  }
</style>
</head>
<body>
<main class="stage">
  <section class="card card--front" aria-label="Business card front">
    <svg class="card__accent" viewBox="0 0 540 300" preserveAspectRatio="none" aria-hidden="true">
      <polygon points="0,0 120,0 0,105" fill="var(--red)"/>
      <polygon points="540,175 540,300 440,300" fill="var(--white)"/>
    </svg>
    <div class="front__brand">Varemo Group</div>
    <div class="front__identity">
      <div class="front__name">Rohesh Kumbar</div>
      <div class="front__title">President / CEO</div>
    </div>
    <ul class="contact">
      <li class="contact__row">
        <svg class="contact__icon" viewBox="0 0 12 12" aria-hidden="true"><path d="M6 0a4 4 0 0 0-4 4c0 3 4 8 4 8s4-5 4-8a4 4 0 0 0-4-4zm0 5.5A1.5 1.5 0 1 1 6 2.5a1.5 1.5 0 0 1 0 3z"/></svg>
        <span>4100 Lindell Ave</span>
      </li>
      <li class="contact__row">
        <svg class="contact__icon contact__icon--empty" viewBox="0 0 12 12" aria-hidden="true"></svg>
        <span>Tampa, FL 33611</span>
      </li>
      <li class="contact__row">
        <svg class="contact__icon" viewBox="0 0 12 12" aria-hidden="true"><path d="M3 0h6a1 1 0 0 1 1 1v10a1 1 0 0 1-1 1H3a1 1 0 0 1-1-1V1a1 1 0 0 1 1-1zm0 1.5v8h6v-8z"/></svg>
        <span>727.418.9062</span>
      </li>
      <li class="contact__row">
        <svg class="contact__icon" viewBox="0 0 12 12" aria-hidden="true"><path d="M0 2h12v8H0zm1 1l5 4 5-4z"/></svg>
        <span>roheshkumbar@varemo.com</span>
      </li>
      <li class="contact__row">
        <svg class="contact__icon" viewBox="0 0 12 12" aria-hidden="true"><circle cx="6" cy="6" r="6"/><path d="M0.5 6h11M6 0.5c-3 3-3 8 0 11M6 0.5c3 3 3 8 0 11" stroke="var(--card)" stroke-width="0.8" fill="none"/></svg>
        <span>www.varemo.com</span>
      </li>
    </ul>
  </section>

  <section class="card card--back" aria-label="Business card back">
    <div class="back__brand">Varemo Group</div>
  </section>
</main>
</body>
</html>
```